PEAK KENNEL - business card
A way to remember us and buy our products
Professional
PEAKKENNEL - the finest pick
Lindmarkv. 24
SE-712 46 Eskilstuna
SWEDEN
info@peakkennel-demo.se
www.peakkennel-demo.se
I would like the business cards and other material to match.
It is about dogs and our show trolley.
I need something to hand out as I meet people at dog shows or otherwise.
your ideas are welcome to figure out what the backside should be.
drawing of product_logo related
LOGO in whole, van be split into two
4 berth
LOGO PDF
drawing pdf
Product today. Steel 2 berth

```html
<!DOCTYPE html>
<html lang="en">
<head>
<meta charset="utf-8">
<title>PeakKennel Stationery Set</title>
<link rel="stylesheet" href="https://fonts.googleapis.com/css2?family=Open+Sans:wght@400;600;800&display=swap">
<style>
:root{
  --navy:#1b4f8c;
  --navy-dark:#123a6a;
  --orange:#f08a1c;
  --paper:#ffffff;
  --ink:#333333;
  --muted:#8a8a8a;
  --line:#c9c9c9;
  --ghost:#e6edf5;
  --stage:#eceae6;
}
*{box-sizing:border-box;margin:0;padding:0}
html,body{width:1200px;height:562px;overflow:hidden}
body{background:var(--stage);font-family:"Open Sans",Arial,sans-serif;color:var(--ink);position:relative}
.piece{position:absolute}
.piece-label{position:absolute;left:0;right:0;top:-15px;text-align:center;font-size:8px;font-weight:600;color:#333}
.sheet{background:var(--paper);box-shadow:0 1px 4px rgba(0,0,0,.25);position:relative;width:100%;height:100%;overflow:hidden}
.brand{display:flex;align-items:center;gap:6px;font-weight:800;color:var(--navy);letter-spacing:.5px}
.brand-dot{border-radius:50%;background:var(--orange);flex:none}
.footer-wave{position:absolute;left:0;bottom:0;width:100%;height:42px}
.footer-text{position:absolute;left:0;right:0;bottom:7px;text-align:center;font-size:5px;color:#fff;word-spacing:2px}
.ghost-mark{position:absolute;display:flex;flex-direction:column;align-items:center;gap:10px}
.ghost-circle{width:150px;height:150px;border-radius:50%;background:var(--ghost)}
.ghost-name{font-weight:800;font-size:20px;color:var(--ghost);letter-spacing:1px}

/* Fax cover */
.fax{left:34px;top:29px;width:364px;height:518px}
.fax .brand{position:absolute;left:24px;top:18px;font-size:24px}
.fax .brand-dot{width:26px;height:26px}
.fax-title{position:absolute;right:22px;top:62px;font-size:8px;font-weight:800;color:#333}
.fax-table{position:absolute;left:22px;top:72px;width:320px;display:grid;grid-template-columns:1fr 1fr;column-gap:14px}
.fax-field{display:flex;align-items:flex-end;height:19px;border-bottom:1px solid var(--line);font-size:6.5px;color:#555}
.fax-field span{width:44px}
.fax-table{border-top:1px solid var(--line);border-left:1px solid var(--line);border-right:1px solid var(--line)}
.fax-options{position:absolute;left:22px;top:160px;width:320px;display:flex;justify-content:space-between;font-size:6px;color:#555}
.fax-options label{display:flex;align-items:center;gap:3px}
.box{width:6px;height:6px;border:1px solid #888}
.fax .ghost-mark{left:107px;top:250px}

/* Letterhead */
.letterhead{left:413px;top:29px;width:379px;height:518px}
.letterhead .brand{position:absolute;left:0;right:0;justify-content:center;top:20px;font-size:26px}
.letterhead .brand-dot{width:28px;height:28px}
.letterhead .ghost-mark{left:114px;top:250px}

/* Business cards */
.card-front{left:810px;top:36px;width:152px;height:90px}
.card-front .sheet{background:var(--navy)}
.card-front .card-band{position:absolute;right:0;top:0;width:92px;height:100%;background:var(--paper);border-radius:40px 0 0 40px}
.card-front .brand{position:absolute;right:8px;top:26px;font-size:11px}
.card-front .brand-dot{width:11px;height:11px}
.card-person{position:absolute;left:6px;top:36px;color:#fff;font-size:5px;line-height:1.5}
.card-person strong{font-size:6px;display:block}
.card-contact{position:absolute;right:8px;top:48px;font-size:4px;color:#555;line-height:1.5;text-align:right}
.card-back{left:975px;top:36px;width:190px;height:90px}
.card-back .brand{position:absolute;left:0;right:0;justify-content:center;top:18px;font-size:17px}
.card-back .brand-dot{width:16px;height:16px}
.card-tagline{position:absolute;left:0;right:0;top:44px;text-align:center;font-size:6px;color:#555}

/* Envelopes */
.env-front{left:804px;top:149px;width:372px;height:192px}
.env-front .brand{position:absolute;left:16px;top:14px;font-size:20px}
.env-front .brand-dot{width:22px;height:22px}
.env-address{position:absolute;left:16px;top:44px;font-size:5px;color:#555}
.env-back{left:804px;top:384px;width:372px;height:163px}
.env-back .flap{position:absolute;inset:0;width:100%;height:100%}
.env-back .flap-dot{position:absolute;left:176px;top:82px;width:20px;height:20px;border-radius:50%;background:var(--orange)}
</style>
</head>
<body>

<section class="piece fax">
  <div class="piece-label">Fax Cover</div>
  <div class="sheet">
    <div class="brand"><span class="brand-dot"></span>PEAKKENNEL</div>
    <div class="fax-title">FAX</div>
    <div class="fax-table">
      <div class="fax-field"><span>To :</span></div><div class="fax-field"><span>From :</span></div>
      <div class="fax-field"><span>Fax :</span></div><div class="fax-field"><span>Pages :</span></div>
      <div class="fax-field"><span>Phone :</span></div><div class="fax-field"><span>Date :</span></div>
      <div class="fax-field"><span>Re :</span></div><div class="fax-field"><span>CC :</span></div>
    </div>
    <div class="fax-options">
      <label><i class="box"></i>Urgent</label>
      <label><i class="box"></i>For Review</label>
      <label><i class="box"></i>Please Comment</label>
      <label><i class="box"></i>Please Reply</label>
      <label><i class="box"></i>Please Recycle</label>
    </div>
    <div class="ghost-mark" aria-hidden="true"><div class="ghost-circle"></div><div class="ghost-name">PEAKKENNEL</div></div>
    <svg class="footer-wave" viewBox="0 0 380 42" preserveAspectRatio="none" aria-hidden="true">
      <path d="M0 16 C100 4 220 30 380 10 L380 42 L0 42Z" fill="var(--orange)"/>
      <path d="M0 20 C100 8 220 34 380 14 L380 42 L0 42Z" fill="var(--navy)"/>
    </svg>
    <div class="footer-text">Lindmarkv. 24, SE-712 46 Eskilstuna &nbsp; Tel: +46 16 555 0142 &nbsp; info@peakkennel-demo.se</div>
  </div>
</section>

<section class="piece letterhead">
  <div class="piece-label">Letterhead</div>
  <div class="sheet">
    <div class="brand"><span class="brand-dot"></span>PEAKKENNEL</div>
    <div class="ghost-mark" aria-hidden="true"><div class="ghost-circle"></div><div class="ghost-name">PEAKKENNEL</div></div>
    <svg class="footer-wave" viewBox="0 0 380 42" preserveAspectRatio="none" aria-hidden="true">
      <path d="M0 16 C100 4 220 30 380 10 L380 42 L0 42Z" fill="var(--orange)"/>
      <path d="M0 20 C100 8 220 34 380 14 L380 42 L0 42Z" fill="var(--navy)"/>
    </svg>
    <div class="footer-text">Lindmarkv. 24, SE-712 46 Eskilstuna &nbsp; Tel: +46 16 555 0142 &nbsp; www.peakkennel-demo.se</div>
  </div>
</section>

<section class="piece card-front">
  <div class="piece-label">Business Card (Front)</div>
  <div class="sheet">
    <div class="card-band"></div>
    <div class="card-person"><strong>Anna Berg</strong>Sales Manager</div>
    <div class="brand"><span class="brand-dot"></span>PEAKKENNEL</div>
    <div class="card-contact">Lindmarkv. 24, SE-712 46<br>info@peakkennel-demo.se<br>www.peakkennel-demo.se</div>
  </div>
</section>

<section class="piece card-back">
  <div class="piece-label">Business Card (Back)</div>
  <div class="sheet">
    <div class="brand"><span class="brand-dot"></span>PEAKKENNEL</div>
    <div class="card-tagline">the finest pick</div>
    <svg class="footer-wave" viewBox="0 0 380 42" preserveAspectRatio="none" aria-hidden="true" style="height:24px">
      <path d="M0 16 C100 4 220 30 380 10 L380 42 L0 42Z" fill="var(--orange)"/>
      <path d="M0 20 C100 8 220 34 380 14 L380 42 L0 42Z" fill="var(--navy)"/>
    </svg>
  </div>
</section>

<section class="piece env-front">
  <div class="piece-label">Envelope (Front)</div>
  <div class="sheet">
    <div class="brand"><span class="brand-dot"></span>PEAKKENNEL</div>
    <div class="env-address">Lindmarkv. 24, SE-712 46 Eskilstuna, SWEDEN</div>
    <svg class="footer-wave" viewBox="0 0 380 42" preserveAspectRatio="none" aria-hidden="true" style="height:46px">
      <path d="M0 16 C100 4 220 30 380 10 L380 42 L0 42Z" fill="var(--orange)"/>
      <path d="M0 20 C100 8 220 34 380 14 L380 42 L0 42Z" fill="var(--navy)"/>
    </svg>
  </div>
</section>

<section class="piece env-back">
  <div class="piece-label">Envelope (Back)</div>
  <div class="sheet">
    <svg class="flap" viewBox="0 0 372 163" preserveAspectRatio="none" aria-hidden="true">
      <path d="M0 0 L186 92 L372 0" fill="none" stroke="#bfbfbf" stroke-width="1"/>
      <path d="M0 163 L150 80 M372 163 L222 80" fill="none" stroke="#d8d8d8" stroke-width="1"/>
    </svg>
    <div class="flap-dot"></div>
  </div>
</section>

</body>
</html>
```